Birchfield Dental Care Stationery

create stationery, business cards and envelops for business. Use current logo on website but open to new fonts for the business name. Business name is Birchfield Dental Care, would like below the name added "Cosmetic - Family - Implants" Website is www.birchfielddentalcareQX.example. I would like to have modern look, clean, and professional. The water mark of the logo is a great thing to ad as well.

Target Market(s)

General public, Families, Cosmetic, Implant

Industry/Entity Type

Dental

Font styles to use
Sans Serif

Colors
9bcb3c
000000
757575
c9c9c9

Requirements
Must have
• Would like to see different versions of the current logo. Improvements, color, sytle, and class.
Nice to have
• current font has double "oo" in the Birchfield logo, does not need to have with new logo.

```html
<!DOCTYPE html>
<html lang="en">
<head>
<meta charset="utf-8">
<title>Birchfield Dental Care Stationery</title>
<link href="https://fonts.googleapis.com/css2?family=Montserrat:wght@400;500;600&display=swap" rel="stylesheet">
<style>
:root{
  --green:#9bcb3c;
  --black:#000000;
  --ink:#222222;
  --grey:#757575;
  --light:#c9c9c9;
  --strip:#dcdcdc;
  --mark:#f1f1f1;
  --stage:#b5b5b5;
  --paper:#ffffff;
}
*{margin:0;padding:0;box-sizing:border-box}
html,body{width:1200px;height:2198px;overflow:hidden}
body{background:var(--stage);font-family:"Montserrat",Arial,sans-serif;color:var(--ink);position:relative}
.sheet{position:absolute;background:var(--paper);overflow:hidden;box-shadow:0 3px 10px rgba(0,0,0,.28)}
.band{position:absolute;left:0;top:0;bottom:0;background:var(--green)}
.band-edge{position:absolute;top:0;bottom:0;width:5px;background:var(--strip)}
.brand{position:absolute;display:flex;align-items:center}
.brand-ring{border-radius:50%;border:4px solid var(--green);flex:none}
.brand-text{margin-left:12px}
.brand-name{font-weight:500;text-transform:uppercase;color:var(--ink);line-height:1;letter-spacing:.01em;white-space:nowrap}
.brand-tag{font-weight:500;color:var(--ink);margin-top:4px;white-space:nowrap}
.watermark{position:absolute;border-radius:50%;border:16px solid var(--mark)}
.small{font-size:12px;line-height:14.5px;color:var(--ink)}
.icons{position:absolute;display:flex;flex-direction:column}
.icons svg{display:block;fill:var(--paper)}

/* letterhead */
.letterhead{left:142px;top:88px;width:916px;height:1187px}
.letterhead .band{width:34px}
.letterhead .band-edge{left:34px}
.letterhead .brand{left:83px;top:22px}
.letterhead .brand-ring{width:96px;height:96px}
.letterhead .brand-name{font-size:28px}
.letterhead .brand-tag{font-size:11.5px}
.letterhead .sender{position:absolute;right:40px;top:62px;text-align:right}
.letterhead .contacts{position:absolute;left:62px;top:1108px}
.letterhead .icons{left:11px;top:1111px;gap:3.5px}
.letterhead .watermark{left:532px;top:806px;width:380px;height:380px}

/* envelope */
.envelope{left:88px;top:1362px;width:1025px;height:444px}
.envelope .band{width:37px}
.envelope .band-edge{left:37px}
.envelope .brand{left:63px;top:20px}
.envelope .brand-ring{width:88px;height:88px}
.envelope .brand-name{font-size:26px}
.envelope .brand-tag{font-size:11px}
.envelope .return{position:absolute;left:63px;top:136px}
.envelope .watermark{left:637px;top:66px;width:366px;height:366px}

/* business cards */
.card{top:1894px;width:378px;height:216px}
.card-front{left:201px;background:var(--green)}
.card-front .front-ring{position:absolute;left:-12px;top:18px;width:176px;height:176px;border-radius:50%;border:5px solid var(--paper)}
.card-front .front-name{position:absolute;left:178px;top:86px;color:var(--paper)}
.card-front .brand-name{color:var(--paper);font-size:22px}
.card-front .brand-tag{color:var(--paper);font-size:9.5px}
.card-back{left:623px}
.card-back .band{width:36px}
.card-back .band-edge{left:36px}
.card-back .brand{left:168px;top:18px}
.card-back .brand-ring{width:62px;height:62px;border-width:3px}
.card-back .brand-text{margin-left:8px}
.card-back .brand-name{font-size:17px}
.card-back .brand-tag{font-size:7.5px;margin-top:3px}
.card-back .holder{position:absolute;left:52px;top:119px}
.card-back .holder-name{font-size:12px;font-weight:600;color:var(--black);margin-bottom:4px}
.card-back .holder-lines{font-size:10px;line-height:13px}
.card-back .icons{left:13px;top:136px;gap:3px}
</style>
</head>
<body>

<section class="sheet letterhead" aria-label="Letterhead">
  <div class="band"></div><div class="band-edge"></div>
  <div class="brand">
    <div class="brand-ring"></div>
    <div class="brand-text">
      <div class="brand-name">Birchfield<br>Dental Care</div>
      <div class="brand-tag">Cosmetic - Family - Implants</div>
    </div>
  </div>
  <address class="sender small" style="font-style:normal">1182 North Birchfield Road<br>Quarry Vale, QX 00421</address>
  <div class="icons">
    <svg width="10" height="11" viewBox="0 0 10 10"><path d="M2 0l2 2.5-1 1.2c.6 1.3 1.6 2.3 2.9 2.9l1.2-1L10 7.6 8.6 10C4 9.6.4 6 0 1.4z"/></svg>
    <svg width="10" height="11" viewBox="0 0 10 10"><rect x="2" y="0" width="6" height="3"/><rect x="0" y="3.5" width="10" height="4"/><rect x="2" y="7" width="6" height="3"/></svg>
    <svg width="10" height="11" viewBox="0 0 10 10"><path d="M0 2h10v6H0z M0 2l5 3.5L10 2" /></svg>
    <svg width="10" height="11" viewBox="0 0 10 10"><path d="M4 6l2-2M3 5L1.5 6.5a1.8 1.8 0 002.5 2.5L5.5 7.5M7 5l1.5-1.5A1.8 1.8 0 006 1L4.5 2.5" stroke="#fff" stroke-width="1.3" fill="none"/></svg>
  </div>
  <div class="contacts small">(555) 014-2280<br>(555) 014-2291<br>info@birchfielddentalcareQX.example<br>www.birchfielddentalcareQX.example</div>
  <div class="watermark"></div>
</section>

<section class="sheet envelope" aria-label="Envelope">
  <div class="band"></div><div class="band-edge"></div>
  <div class="brand">
    <div class="brand-ring"></div>
    <div class="brand-text">
      <div class="brand-name">Birchfield<br>Dental Care</div>
      <div class="brand-tag">Cosmetic - Family - Implants</div>
    </div>
  </div>
  <address class="return small" style="font-style:normal">1182 North Birchfield Road<br>Quarry Vale, QX 00421</address>
  <div class="watermark"></div>
</section>

<section class="sheet card card-front" aria-label="Business card front">
  <div class="front-ring"></div>
  <div class="front-name">
    <div class="brand-name">Birchfield<br>Dental Care</div>
    <div class="brand-tag">Cosmetic - Family - Implants</div>
  </div>
</section>

<section class="sheet card card-back" aria-label="Business card back">
  <div class="band"></div><div class="band-edge"></div>
  <div class="brand">
    <div class="brand-ring"></div>
    <div class="brand-text">
      <div class="brand-name">Birchfield<br>Dental Care</div>
      <div class="brand-tag">Cosmetic - Family - Implants</div>
    </div>
  </div>
  <div class="icons">
    <svg width="9" height="10" viewBox="0 0 10 10"><path d="M5 0a3.5 3.5 0 013.5 3.5C8.5 6 5 10 5 10S1.5 6 1.5 3.5A3.5 3.5 0 015 0z"/></svg>
    <svg width="9" height="10" viewBox="0 0 10 10"><path d="M2 0l2 2.5-1 1.2c.6 1.3 1.6 2.3 2.9 2.9l1.2-1L10 7.6 8.6 10C4 9.6.4 6 0 1.4z"/></svg>
    <svg width="9" height="10" viewBox="0 0 10 10"><rect x="2" y="0" width="6" height="3"/><rect x="0" y="3.5" width="10" height="4"/><rect x="2" y="7" width="6" height="3"/></svg>
    <svg width="9" height="10" viewBox="0 0 10 10"><path d="M0 2h10v6H0z"/></svg>
    <svg width="9" height="10" viewBox="0 0 10 10"><path d="M4 6l2-2M3 5L1.5 6.5a1.8 1.8 0 002.5 2.5L5.5 7.5M7 5l1.5-1.5A1.8 1.8 0 006 1L4.5 2.5" stroke="#fff" stroke-width="1.3" fill="none"/></svg>
  </div>
  <div class="holder">
    <div class="holder-name">Martin L. Okafor D.D.S.</div>
    <div class="holder-lines">1182 North Birchfield Rd. Quarry Vale, QX 00421<br>(555) 014-2280<br>(555) 014-2291<br>martin@birchfielddentalcareQX.example<br>www.birchfielddentalcareQX.example</div>
  </div>
</section>

</body>
</html>
```